Business Cards for an engineering & contracting company
Korvane Group
Business Cards for an engineering & contracting company - Architecture
Creative Brief
Professional
Architect Marwan Tarek Korvane
CEO - Project Manager
Chiyah, Blvd Rue Doumani, Next to Meridel Plaza, Korvane Tower, Blk B - 2nd floor
marwan@korvanegroup-example.com
www.korvanegroup-example.com
the word "Architect" can be written in a nice design before the name, The name is "Marwan Tarek Korvane". The company name is "Korvane Group" The country is " Beirut, Lebanon" Its preferable is the card is made of 2 or 3 colors that make it impressive
A design that is related to the company description, which is (architecture, engineering, design, contracting and construction) The logo may be a solution if its alone or with something else added to it.
Korvane Korvane
I'd like to see other stationery designs too in addition to the business card.

```html
<!DOCTYPE html>
<html lang="en">
<head>
<meta charset="utf-8">
<title>Korvane Group — Stationery</title>
<link href="https://fonts.googleapis.com/css2?family=Cinzel:wght@600&family=Open+Sans:wght@400;600&display=swap" rel="stylesheet">
<style>
  :root{
    --blue:#1f6fe3;
    --grey:#9aa0a8;
    --grey-light:#c9cdd3;
    --ink:#4a4f57;
    --paper:#ffffff;
    --backdrop:#eef0f3;
  }
  *{margin:0;padding:0;box-sizing:border-box}
  html,body{width:1200px;height:936px;overflow:hidden;background:var(--backdrop)}
  body{position:relative;font-family:"Open Sans",Arial,sans-serif;color:var(--ink)}
  .sheet{position:absolute;background:var(--paper);box-shadow:0 3px 10px rgba(0,0,0,.14);overflow:hidden}
  .sheet > svg.swoosh{position:absolute;inset:0;width:100%;height:100%}
  .brand{position:absolute;display:flex;flex-direction:column;align-items:center;text-align:center}
  .brand-row{display:flex;align-items:center;gap:6px}
  .brand-square{background:var(--blue);display:block}
  .brand-name{font-family:"Cinzel",Georgia,serif;font-weight:600;color:var(--blue);letter-spacing:.04em;white-space:nowrap}
  .brand-tagline{font-family:"Cinzel",Georgia,serif;font-weight:600;color:var(--grey);letter-spacing:.12em;white-space:nowrap}

  /* Letterhead */
  .letterhead{left:30px;top:30px;width:550px;height:577px}
  .letterhead .brand{left:34px;top:58px}
  .letterhead .brand-square{width:14px;height:14px}
  .letterhead .brand-name{font-size:13px}
  .letter-body{position:absolute;left:40px;top:150px;width:380px;font-size:7px;line-height:1.55}
  .letter-body p{margin-bottom:9px}
  .signature{width:60px;height:20px;background:linear-gradient(90deg,#d9dce1,#eceef1);margin:4px 0 6px;border-radius:2px}
  .letter-contact{position:absolute;right:10px;bottom:28px;width:70px;color:#fff;font-size:5px;line-height:1.55;text-align:right;white-space:nowrap}

  /* Folder */
  .folder{left:632px;top:30px;width:538px;height:577px}
  .folder .brand{left:0;right:0;top:240px}
  .folder .brand-square{width:30px;height:30px}
  .folder .brand-name{font-size:30px}
  .folder .brand-tagline{font-size:11px;margin-top:4px}
  .folder-url{position:absolute;right:40px;bottom:30px;color:#fff;font-size:10px;letter-spacing:.2em}

  /* Business cards */
  .card{width:190px;height:109px;left:50px}
  .card-detail{top:663px}
  .card-logo{top:792px}
  .card-detail .brand{left:12px;top:22px}
  .card-detail .brand-square{width:8px;height:8px}
  .card-detail .brand-name{font-size:8px}
  .card-info{position:absolute;left:78px;top:12px;width:106px;font-size:4.8px;line-height:1.45;text-align:left}
  .card-info .person{font-weight:600;color:var(--blue);font-size:5.8px;white-space:nowrap}
  .card-info .role{color:var(--grey);margin-bottom:3px}
  .card-logo .brand{left:0;right:0;top:38px}
  .card-logo .brand-square{width:10px;height:10px}
  .card-logo .brand-name{font-size:11px}
  .card-logo .brand-tagline{font-size:4.5px;margin-top:2px}

  /* Envelopes */
  .envelope-front{left:266px;top:663px;width:422px;height:235px}
  .envelope-front .brand{left:0;right:0;top:60px}
  .envelope-front .brand-square{width:14px;height:14px}
  .envelope-front .brand-name{font-size:16px}
  .envelope-front .brand-tagline{font-size:6px;margin-top:3px}
  .envelope-address{position:absolute;left:0;right:0;top:112px;text-align:center;font-size:5.5px;color:var(--grey)}
  .envelope-back{left:734px;top:663px;width:436px;height:235px}
  .envelope-url{position:absolute;right:60px;top:30px;color:#fff;font-size:9px;letter-spacing:.2em}
</style>
</head>
<body>

<section class="sheet letterhead">
  <svg class="swoosh" viewBox="0 0 550 577" preserveAspectRatio="none" aria-hidden="true">
    <path d="M486 0 C462 200 458 400 466 577 L550 577 L550 0 Z" fill="var(--grey-light)"/>
    <path d="M500 0 C478 200 474 400 482 577 L550 577 L550 0 Z" fill="var(--blue)"/>
  </svg>
  <div class="brand">
    <div class="brand-row"><span class="brand-square"></span><span class="brand-name">KORVANE GROUP</span></div>
  </div>
  <div class="letter-body">
    <p>June 12, 2024</p>
    <p>Nadia Haddad<br>Haddad Holdings</p>
    <p>Dear Nadia,</p>
    <p>We are pleased to submit our proposal for the design and construction of your new residence. Our team brings years of experience in architecture, engineering and contracting across the region.</p>
    <p>Every project is planned with care, from the first sketch to the final handover, so that quality, budget and schedule stay on track.</p>
    <p>Please find the attached plans and cost summary. We would be glad to meet at your convenience to review the details and answer any questions you may have.</p>
    <p>Kind regards,</p>
    <div class="signature" role="img" aria-label="Handwritten signature"></div>
    <p>Marwan Tarek Korvane<br>CEO - Project Manager</p>
  </div>
  <div class="letter-contact">
    Darvesh, Blvd Rue Doumani<br>
    Next to Meridel Plaza<br>
    Korvane Tower, Blk B<br>
    2nd floor<br>
    +961 1 555 010<br>
    marwan@<br>
    korvanegroup-example.com<br>
    www.<br>
    korvanegroup-example.com
  </div>
</section>

<section class="sheet folder">
  <svg class="swoosh" viewBox="0 0 538 577" preserveAspectRatio="none" aria-hidden="true">
    <path d="M440 0 C410 220 330 440 185 577 L538 577 L538 0 Z" fill="var(--grey)"/>
    <path d="M538 30 C480 260 380 460 210 577 L538 577 Z" fill="var(--blue)"/>
  </svg>
  <div class="brand">
    <div class="brand-row"><span class="brand-square"></span><span class="brand-name">KORVANE GROUP</span></div>
    <span class="brand-tagline">BUILT ON SOLID GROUND</span>
  </div>
  <div class="folder-url">www.urwebsitename.com</div>
</section>

<section class="sheet card card-detail">
  <svg class="swoosh" viewBox="0 0 190 109" preserveAspectRatio="none" aria-hidden="true">
    <path d="M190 90 C150 100 110 105 70 109 L190 109 Z" fill="var(--blue)"/>
  </svg>
  <div class="brand">
    <div class="brand-row"><span class="brand-square"></span><span class="brand-name">KORVANE</span></div>
  </div>
  <div class="card-info">
    <div class="person">Architect Marwan Tarek Korvane</div>
    <div class="role">CEO - Project Manager</div>
    <div>+961 1 555 010</div>
    <div>marwan@korvanegroup-example.com</div>
    <div>www.korvanegroup-example.com</div>
    <div>Darvesh, Blvd Rue Doumani, Next to Meridel Plaza, Korvane Tower, Blk B - 2nd floor</div>
  </div>
</section>

<section class="sheet card card-logo">
  <div class="brand">
    <div class="brand-row"><span class="brand-square"></span><span class="brand-name">KORVANE GROUP</span></div>
    <span class="brand-tagline">BUILT ON SOLID GROUND</span>
  </div>
</section>

<section class="sheet envelope-front">
  <svg class="swoosh" viewBox="0 0 422 235" preserveAspectRatio="none" aria-hidden="true">
    <path d="M422 150 C400 190 370 215 330 235 L422 235 Z" fill="var(--grey-light)"/>
    <path d="M422 170 C405 200 385 220 355 235 L422 235 Z" fill="var(--blue)"/>
  </svg>
  <div class="brand">
    <div class="brand-row"><span class="brand-square"></span><span class="brand-name">KORVANE GROUP</span></div>
    <span class="brand-tagline">BUILT ON SOLID GROUND</span>
  </div>
  <div class="envelope-address">Darvesh, Blvd Rue Doumani, Next to Meridel Plaza, Korvane Tower, Blk B - 2nd floor</div>
</section>

<section class="sheet envelope-back">
  <svg class="swoosh" viewBox="0 0 436 235" preserveAspectRatio="none" aria-hidden="true">
    <path d="M0 0 L436 0 L436 96 C330 140 110 140 0 96 Z" fill="var(--grey-light)"/>
    <path d="M0 0 L436 0 L436 86 C330 128 110 128 0 86 Z" fill="var(--blue)"/>
  </svg>
  <div class="envelope-url">www.urwebsitename.com</div>
</section>

</body>
</html>
```